依頼詳細
依頼詳細下記となります。
(1)を一番強調し、(2)の2つは同じ扱いでお願いします。

-------------------------------------------------------------------------------------------------

(1)
ハルネ管理物件内での住み替えは

仲介手数料0円!!(これを特に強調)

(2)
その他にも

[購入を検討のお客さま]
ハルネ管理物件にご入居中のお客さまがハルネで売買物件を購入された場合
仲介手数料10%引き!

[他のエリアに住み替え検討のお客さま]
松江や米子はもちろん全国のお部屋探しもサポートさせて頂きます。
お気軽にご相談ください!

他に必要なキャッチ等あれば入れて頂いてかまいません。
記載項目
抑え※添付ファイル参照
サイズ
A4
ページ数
片面
希望イメージ
シンプル 複雑
単色 カラフル
暗い 明るい
日常 高級
遊び心 厳粛
未来的 伝統的
女性的 男性的
希望する色
水色系、緑系、グレー系、弊社のホームページの色調(グレー、青緑?)
納品ファイル
• イラストレーター形式 (.ai)
補足説明
■ 選んだ理由

社員全員による投票で決定しました。

■ 提案者全員のお礼・コメント

素敵な提案ありがとうございました。

また修正依頼にも迅速に対応頂き感謝します。

また機会がありましたらよろしくお願いします。

```html
<!DOCTYPE html>
<html lang="ja">
<head>
<meta charset="utf-8">
<title>仲介手数料っていくらかかるの？ | ハルネ</title>
<link rel="stylesheet" href="https://fonts.googleapis.com/css2?family=M+PLUS+Rounded+1c:wght@400;700;800&family=Kosugi+Maru&display=swap">
<style>
:root{
  --green:#8cc63f;
  --green-dark:#5fa032;
  --green-pale:#c9e29a;
  --cream:#fbfbe8;
  --stripe-a:#eaf3d4;
  --stripe-b:#f3f8e6;
  --ink:#4a4a4a;
  --ink-soft:#777;
  --accent:#7bb52b;
  --white:#fff;
}
*{box-sizing:border-box;margin:0;padding:0}
html,body{width:846px;height:1200px;overflow:hidden;background:var(--white)}
body{font-family:"M PLUS Rounded 1c","Kosugi Maru",sans-serif;color:var(--ink);position:relative}
p,h1,div,span{white-space:nowrap}

.question{position:absolute;left:0;top:0;width:846px;height:250px;background:var(--green)}
.question .skyline{position:absolute;left:0;bottom:0;width:846px;height:130px;
  background:linear-gradient(180deg,var(--green) 0%,#a6d363 100%)}
.question .q-mark{position:absolute;left:34px;top:22px;font-size:96px;font-weight:800;color:var(--white);line-height:1}
.question .q-text{position:absolute;left:160px;top:50px;font-size:38px;font-weight:700;color:var(--white);letter-spacing:1px}
.question .q-line{position:absolute;left:150px;top:108px;width:520px;height:3px;background:var(--white);border-radius:2px}

.answer{position:absolute;left:0;top:250px;width:846px;height:390px;background:var(--cream)}
.answer .staff{position:absolute;left:30px;top:30px;width:170px;height:280px;border-radius:80px 80px 20px 20px;
  background:linear-gradient(180deg,#e9cbb0 0%,#f2e4d6 45%,#dfe9c6 100%)}
.answer .a-mark{position:absolute;left:215px;top:40px;font-size:62px;font-weight:800;color:var(--accent);line-height:1}
.answer .a-note{position:absolute;left:300px;top:58px;font-size:17px;color:var(--ink-soft)}
.answer .a-lead{position:absolute;left:215px;top:108px;font-size:33px;font-weight:700;color:var(--ink);
  padding-bottom:8px;border-bottom:3px dotted var(--green)}
.answer .fee-tag{position:absolute;left:14px;top:220px;width:250px;height:62px;border-radius:12px;background:var(--green);
  color:var(--white);font-size:34px;font-weight:700;text-align:center;line-height:62px;letter-spacing:2px}
.answer .zero{position:absolute;left:395px;top:135px;font-size:250px;font-weight:800;line-height:1;
  color:var(--white);-webkit-text-stroke:8px var(--accent)}
.answer .mini-staff{position:absolute;left:430px;top:225px;width:50px;height:100px;border-radius:25px 25px 10px 10px;
  background:linear-gradient(180deg,#e9cbb0,#dfe9c6)}
.answer .yen{position:absolute;left:540px;top:250px;font-size:72px;font-weight:800;color:var(--accent);line-height:1.2}
.answer .tail{position:absolute;left:625px;top:285px;font-size:32px;font-weight:700;color:var(--ink)}

.offers{position:absolute;left:0;top:640px;width:846px;height:460px;
  background:repeating-linear-gradient(135deg,var(--stripe-a) 0 10px,var(--stripe-b) 10px 20px)}
.offer{position:absolute;top:18px;width:396px;height:430px}
.offer.buy{left:16px}
.offer.area{left:434px}
.offer .label{display:flex;align-items:center;gap:10px;height:62px;padding:0 16px;background:var(--white);border-radius:31px;font-size:17px;font-weight:700;line-height:1.35}
.offer .label .pre{background:var(--green);color:var(--white);font-size:13px;padding:3px 8px;border-radius:10px;flex:none}
.offer .label em{font-style:normal;color:var(--accent);border-bottom:2px solid var(--accent)}
.offer .staff{position:absolute;left:8px;top:86px;width:90px;height:130px;border-radius:45px 45px 12px 12px;
  background:linear-gradient(180deg,#e9cbb0,#dfe9c6)}
.offer .bubble{position:absolute;left:110px;top:90px;right:0;min-height:90px;background:var(--white);border:2px solid var(--green-pale);
  border-radius:14px;padding:14px 16px;font-size:15px;line-height:1.6;color:var(--ink);white-space:normal}
.offer .result{position:absolute;left:0;right:0;top:250px;text-align:center;font-weight:800;color:var(--ink)}
.offer.buy .result .small{font-size:38px;line-height:1.15;display:inline-block;vertical-align:middle;text-align:left}
.offer.buy .result .big{font-size:96px;color:var(--accent);vertical-align:middle}
.offer.buy .result .off{font-size:44px;vertical-align:middle}
.offer.area .result .nation{display:block;font-size:64px;line-height:1.2}
.offer.area .result .sub{display:block;font-size:32px}

.footer{position:absolute;left:0;top:1100px;width:846px;height:100px;background:var(--white);border-top:3px solid var(--green)}
.footer .brand{position:absolute;top:28px;display:flex;align-items:center;gap:8px;font-weight:800;font-size:22px;color:var(--green-dark)}
.footer .brand.partner{left:20px}
.footer .brand.owner{left:260px}
.footer .brand .dot{width:16px;height:16px;border-radius:50%;background:var(--green-dark)}
.footer .tel{position:absolute;left:430px;top:16px;font-size:28px;font-weight:800;color:var(--green-dark);line-height:1.2}
.footer .tel small{font-size:15px;margin-right:6px}
.footer .web{position:absolute;right:20px;top:28px;font-size:12px;color:var(--ink-soft)}
.footer .address{position:absolute;left:430px;top:58px;font-size:11px;color:var(--ink-soft);line-height:1.5}
</style>
</head>
<body>

<section class="question">
  <div class="skyline" role="img" aria-label="街並みのシルエットイラスト"></div>
  <div class="q-mark">Q.</div>
  <h1 class="q-text">仲介手数料っていくらかかるの？</h1>
  <div class="q-line"></div>
</section>

<section class="answer">
  <div class="staff" role="img" aria-label="案内する女性スタッフのイラスト"></div>
  <div class="a-mark">A.</div>
  <p class="a-note">通常、だいたい１ヶ月のお家賃と同じくらいですが…</p>
  <p class="a-lead">ハルネ管理物件内での住み替えなら</p>
  <div class="fee-tag">仲介手数料</div>
  <div class="zero">0</div>
  <div class="mini-staff" role="img" aria-label="小さな女性スタッフのイラスト"></div>
  <div class="yen">円</div>
  <div class="tail">となります。</div>
</section>

<section class="offers">
  <article class="offer buy">
    <div class="label"><span class="pre">他にも</span><span><em>購入</em>を検討のお客さまは</span></div>
    <div class="staff" role="img" aria-label="女性スタッフのイラスト"></div>
    <p class="bubble">ハルネ管理物件にご入居中のお客さまがハルネで売買物件を購入された場合…</p>
    <p class="result"><span class="small">仲介<br>手数料</span><span class="big">10</span><span class="off">%引き</span></p>
  </article>
  <article class="offer area">
    <div class="label"><span class="pre">さらに</span><span><em>他のエリア</em>に<em>住み替え</em><br>検討のお客さまは</span></div>
    <div class="staff" role="img" aria-label="女性スタッフのイラスト"></div>
    <p class="bubble">松江や米子はもちろん…</p>
    <p class="result"><span class="nation">全国の</span><span class="sub">お部屋探しもサポート</span></p>
  </article>
</section>

<footer class="footer">
  <div class="brand partner"><span class="dot"></span>ヘヤナビショップ</div>
  <div class="brand owner"><span class="dot"></span>ハルネ</div>
  <p class="tel"><small>TEL</small>0854-00-1357</p>
  <p class="web">www.harune-home.jp</p>
  <p class="address">本社 〒690-0000 島根県松江市 中央町 1-2<br>支店 〒683-0000 鳥取県米子市 本町 3-4</p>
</footer>

</body>
</html>
```